2in1 Bartender & Sommelier needs a business card

I need a business card. I worked as a bartender in many places but I just finished a sommelier school and I would like a new business card. I like minimal design, natural materials and something what makes the people think :) I try to be creative in cocktail making, like little mixology, little twist on recipes... I like to travel and discover new places, cultures and of course interesting drinks and improve continously...live a little bit crazy life. And I like what I do...

Target Market(s)

restaurant/winebar managers, winemakers, other sommeliers and bartenders, people who work in food and beverage sector

Industry/Entity Type

Hospitality

Contact Information for Business Card

Rozsa Tarkany
Bartender & Sommelier
Phone: (FR) +33 6 4827 3190
(HU) +36 70 918 6352

Font styles to use
Script

Requirements
Must have
• Some sign, I am a bartender and sommelier as well.
Nice to have
• black and white maybe with 1 or 2 extra color
Should not have
• very colourful, to many things on the card

```html
<!DOCTYPE html>
<html lang="en">
<head>
<meta charset="utf-8">
<title>Rozsa Tarkany – Bartender &amp; Sommelier</title>
<link rel="stylesheet" href="https://fonts.googleapis.com/css2?family=Great+Vibes&display=swap">
<style>
  :root {
    --ink: #0d0d0d;
    --paper: #ffffff;
    --backdrop: #e4e4e6;
    --figure-tone-a: #2a2a2a;
    --figure-tone-b: #4a4a4a;
  }
  * { box-sizing: border-box; margin: 0; padding: 0; }
  html, body {
    width: 1200px;
    height: 800px;
    overflow: hidden;
    background: var(--backdrop);
  }
  .card {
    position: absolute;
    left: 75px;
    top: 100px;
    width: 1050px;
    height: 600px;
    background: var(--paper);
    box-shadow: 0 6px 24px rgba(0,0,0,0.12);
    overflow: hidden;
  }
  .top-bar {
    position: absolute;
    left: 585px;
    top: 0;
    width: 28px;
    height: 118px;
    background: var(--ink);
  }
  .identity {
    position: absolute;
    left: 250px;
    top: 38px;
    width: 330px;
    text-align: center;
    color: var(--ink);
    font-family: "Great Vibes", cursive;
  }
  .identity__name {
    font-size: 68px;
    line-height: 1;
    font-weight: 400;
  }
  .identity__role {
    font-size: 24px;
    line-height: 1.1;
    margin-top: 2px;
  }
  .service-figure {
    position: absolute;
    left: 150px;
    top: 205px;
    width: 250px;
    height: 190px;
    border-radius: 6px;
    background: linear-gradient(135deg, var(--figure-tone-a), var(--figure-tone-b));
  }
  .contact-line {
    position: absolute;
    left: 0;
    top: 0;
  }
  .phones {
    position: absolute;
    left: 680px;
    top: 262px;
    list-style: none;
    color: var(--ink);
    font-family: "Great Vibes", cursive;
    font-size: 27px;
    line-height: 1.25;
  }
</style>
</head>
<body>
  <main class="card">
    <div class="top-bar"></div>

    <header class="identity">
      <h1 class="identity__name">Rozsa Tarkany</h1>
      <p class="identity__role">Bartender &amp; Sommelier</p>
    </header>

    <div class="service-figure" role="img" aria-label="Pictogram of a server in motion carrying a tray with a glass and a small wine card"></div>

    <svg class="contact-line" width="1050" height="600" viewBox="0 0 1050 600" aria-hidden="true">
      <line x1="612" y1="300" x2="612" y2="600" stroke="var(--ink)" stroke-width="5"/>
      <circle cx="612" cy="282" r="46" fill="var(--ink)"/>
      <path d="M600 258 q-8 4 -8 14 q1 20 18 34 q8 6 14 3 l5-4 -10-11 -6 3 q-8-6-11-16 l5-4 -5-14 z"
            fill="var(--paper)"/>
    </svg>

    <ul class="phones">
      <li>+33 6 4827 3190</li>
      <li>+36 70 918 6352</li>
    </ul>
  </main>
</body>
</html>
```